I need a header for the web site www.harlowspipeworks.example/demo
It must include the following
Existig Logo (I will upload the .png)
Text: Serving Calgary and Surrounding Areas for Over 30 Years!
24 Hour Service
Call 403.718.2946 (Note this isn't the actual phone number I will need to be able to change the Phone number once the site is ready to put in a tracking number so I am hoping I get a PSD file with this where the text is editable)
We wnat the feel to be warm and geared more towards a residential customer rather than an industial customer.
We would like blue tones but are open to anything warm.

Size: Aprroximately 960x300

• Rounded Corners to match the content area on the site

```html
<!DOCTYPE html>
<html lang="en">
<head>
<meta charset="utf-8">
<title>Harlow's Pipeworks Ltd — Header</title>
<link rel="stylesheet" href="https://fonts.googleapis.com/css2?family=Stardos+Stencil:wght@700&display=swap">
<style>
  :root {
    --page: #ffffff;
    --panel: #80fbfb;
    --bevel-top: #7fe6df;
    --bevel-side: #66c8c0;
    --bevel-bottom: #4fa39c;
    --bevel-outer: #5aa9a2;
    --ink: #0a0a0a;
  }
  html, body {
    margin: 0;
    padding: 0;
    width: 1200px;
    height: 1200px;
    overflow: hidden;
    background: var(--page);
  }
  .canvas {
    position: relative;
    width: 1200px;
    height: 1200px;
    font-family: "Stardos Stencil", "Times New Roman", serif;
    font-weight: 700;
    color: var(--ink);
  }
  .header-banner {
    position: absolute;
    left: 7px;
    top: 363px;
    width: 922px;
    height: 274px;
  }
  .header-banner svg {
    position: absolute;
    inset: 0;
    display: block;
  }
  .brand-name {
    position: absolute;
    left: 60px;
    top: 64px;
    width: 400px;
    text-align: center;
    font-size: 32px;
    line-height: 1;
    letter-spacing: 0.5px;
    margin: 0;
  }
  .service-title {
    position: absolute;
    left: 450px;
    top: 30px;
    width: 430px;
    text-align: center;
    font-size: 47px;
    line-height: 1;
    margin: 0;
  }
  .service-call {
    position: absolute;
    left: 489px;
    top: 107px;
    font-size: 34px;
    line-height: 1;
    letter-spacing: 0.5px;
    margin: 0;
  }
  .service-area {
    position: absolute;
    left: 60px;
    top: 200px;
    font-size: 28px;
    line-height: 1;
    margin: 0;
  }
</style>
</head>
<body>
<div class="canvas">
  <header class="header-banner">
    <svg width="922" height="274" viewBox="0 0 922 274" aria-hidden="true">
      <rect x="0" y="0" width="922" height="274" rx="6" fill="var(--bevel-outer)"/>
      <polygon points="3,3 919,3 905,16 17,16" fill="var(--bevel-top)"/>
      <polygon points="3,3 17,16 17,258 3,271" fill="var(--bevel-side)"/>
      <polygon points="919,3 919,271 905,258 905,16" fill="var(--bevel-side)"/>
      <polygon points="3,271 17,258 905,258 919,271" fill="var(--bevel-bottom)"/>
      <rect x="17" y="16" width="888" height="242" fill="var(--panel)"/>
    </svg>
    <p class="brand-name">HARLOW'S PIPEWORKS LTD</p>
    <h1 class="service-title">24 Hour Service</h1>
    <p class="service-call">Call 403.718.2946</p>
    <p class="service-area">Serving Calgary and Surrounding Areas for Over 30 Years</p>
  </header>
</div>
</body>
</html>
```